PowerPoint Template - Multiple Slide Backgrounds

Looking for a professional PowerPoint template for a technology company. You will see with the logo there's sort of a theme with gears and a lightbulb of sorts. Keeping with this sort of design could help with the brand.

Branding information
• Logo with transparent background included
• Primary Color (Orange) Hex #E6753D
• Secondary Color (Brown) Hex #6A4238
• Primary Font - Myriad Pro
• Secondary Font - Quiet Sans Light

Design request -
• PowerPoint (POTX) template with master slide views
• Cover Slide
• Color Pallet - 7 Color PowerPoint pallet that includes and complements primary and secondary colors
• Slide Master with Footer
• Multiple Background Types to allow for smart art overlay or bullet point text boxes
Bonus - Sample graphical elements using shapes and smart art

```html
<!DOCTYPE html>
<html lang="en">
<head>
<meta charset="UTF-8">
<title>Bullet Slides</title>
<link rel="stylesheet" href="https://fonts.googleapis.com/css2?family=Source+Sans+3:wght@300;400;600;700&display=swap">
<style>
  :root {
    --orange: #e6753d;
    --brown: #6a4238;
    --body-text: #7a7a7a;
    --rule: #c9c9c9;
    --footer-band: #efefef;
    --footer-text: #444444;
    --faint: #f6f6f6;
    --paper: #ffffff;
  }
  * { margin: 0; padding: 0; box-sizing: border-box; }
  html, body { width: 1200px; height: 653px; overflow: hidden; background: var(--paper); }
  body { font-family: "Source Sans 3", sans-serif; }
  .slide { position: relative; width: 1200px; height: 653px; overflow: hidden; background: var(--paper); }

  .backdrop-ring { position: absolute; left: 720px; top: 110px; width: 500px; height: 500px; }

  .guide-line { position: absolute; left: 64px; top: 0; width: 1px; height: 225px; background: var(--rule); }
  .title-bar { position: absolute; left: 59px; top: 66px; width: 7px; height: 86px; background: var(--orange); border-radius: 3px; }

  .title-block { position: absolute; left: 91px; top: 74px; }
  .subtitle { font-size: 28px; font-weight: 400; color: var(--orange); line-height: 1.05; }
  .title { font-size: 37px; font-weight: 700; color: var(--brown); line-height: 1.1; }

  .brand { position: absolute; right: 16px; top: 30px; display: flex; align-items: center; gap: 8px; }
  .brand-dot { width: 20px; height: 20px; border-radius: 50%; background: var(--orange); }
  .brand-name { font-size: 22px; font-weight: 700; color: var(--brown); }

  .bullets { position: absolute; left: 92px; top: 186px; width: 1000px; list-style: none; }
  .bullet { margin-bottom: 32px; }
  .bullet-head { display: flex; align-items: center; gap: 14px; }
  .bullet-mark { width: 26px; height: 26px; border-radius: 50%; background: var(--brown); flex: none; }
  .bullet-title { font-size: 27px; font-weight: 700; color: var(--orange); line-height: 1.2; }
  .bullet-body { margin-left: 44px; font-size: 17.5px; font-weight: 300; color: var(--body-text); line-height: 27px; }

  .footer { position: absolute; left: 0; bottom: 0; width: 1200px; height: 36px; background: var(--footer-band); }
  .copyright { position: absolute; left: 19px; top: 7px; font-size: 18px; color: var(--footer-text); }
  .page-number { position: absolute; right: 14px; top: -4px; width: 38px; height: 38px; border-radius: 50%; background: var(--orange); color: var(--paper); font-size: 17px; font-weight: 700; display: flex; align-items: center; justify-content: center; }
</style>
</head>
<body>
<div class="slide">
  <svg class="backdrop-ring" viewBox="0 0 500 500" aria-hidden="true">
    <circle cx="250" cy="250" r="200" fill="none" stroke="var(--faint)" stroke-width="60"/>
  </svg>

  <div class="guide-line"></div>
  <div class="title-bar"></div>

  <header class="title-block">
    <p class="subtitle">Subtitle Here</p>
    <h1 class="title">Bullet Slides</h1>
  </header>

  <div class="brand">
    <span class="brand-dot"></span>
    <span class="brand-name">Cogwell</span>
  </div>

  <ul class="bullets">
    <li class="bullet">
      <div class="bullet-head"><span class="bullet-mark"></span><h2 class="bullet-title">Bullet text Here</h2></div>
      <p class="bullet-body">Lorem Ipsum is simply dummy text of the printing and typesetting industry. Lorem Ipsum has been the industry's standard dummy text ever since the 1500s, when an unknown printer took a galley of type and scrambled it to make a type specimen book.</p>
    </li>
    <li class="bullet">
      <div class="bullet-head"><span class="bullet-mark"></span><h2 class="bullet-title">Bullet text Here</h2></div>
      <p class="bullet-body">Lorem Ipsum is simply dummy text of the printing and typesetting industry. Lorem Ipsum has been the industry's standard dummy text ever since the 1500s, when an unknown printer took a galley of type and scrambled it to make a type specimen book.</p>
    </li>
    <li class="bullet">
      <div class="bullet-head"><span class="bullet-mark"></span><h2 class="bullet-title">Bullet text Here</h2></div>
      <p class="bullet-body">Lorem Ipsum is simply dummy text of the printing and typesetting industry. Lorem Ipsum has been the industry's standard dummy text ever since the 1500s, when an unknown printer took a galley of type and scrambled it to make a type specimen book.</p>
    </li>
  </ul>

  <footer class="footer">
    <span class="copyright">Copyright text here</span>
    <span class="page-number">01</span>
  </footer>
</div>
</body>
</html>
```